Website for Party

Design a new website for PlumtreeGatherings.net
We have attached the new logos and please look at the website, and our facebook page: facebook.com/plumtreegatherings for inspiration
Updates

Hi Guys, please be original with all designs and images otherwise the design will be eliminated Thank you

some of your designs have too much happening in them, others make it clear that the designer has not yet read the brief fully

Please everyone be original!

```html
<!DOCTYPE html>
<html lang="en">
<head>
<meta charset="utf-8">
<title>Plumtree Gatherings</title>
<link href="https://fonts.googleapis.com/css2?family=Arimo:wght@400;700&display=swap" rel="stylesheet">
<style>
  :root {
    --page-bg: #ffffff;
    --panel-dark: #121212;
    --panel-glass: rgba(40, 40, 40, 0.55);
    --logo-bg: #000000;
    --text-main: #ffffff;
    --text-sub: #a9a9a9;
    --divider: #3a3a3a;
    --icon-bg: #333333;
    --icon-fg: #121212;
    --copy-text: #6a6a6a;
  }
  * { margin: 0; padding: 0; box-sizing: border-box; }
  html, body {
    width: 1200px; height: 1000px; overflow: hidden;
    background: var(--page-bg);
    font-family: "Arimo", Arial, sans-serif;
  }
  .site { position: relative; width: 1200px; height: 1000px; }
  .hero {
    position: absolute; left: 0; top: 208px; width: 1200px; height: 578px;
    background:
      radial-gradient(ellipse 420px 300px at 560px 300px, #ffe9a8 0%, #ffc04a 35%, rgba(240,130,20,0.9) 65%, rgba(120,50,5,0) 100%),
      radial-gradient(ellipse 260px 220px at 1050px 420px, rgba(255,170,60,0.75), rgba(0,0,0,0) 100%),
      linear-gradient(180deg, #6b2a05 0%, #b55410 30%, #8a3a08 60%, #1a0c04 88%, #0a0806 100%);
  }
  .sidebar {
    position: absolute; left: 44px; top: 208px; width: 196px; height: 578px;
    background: var(--panel-glass);
  }
  .sidebar-body {
    position: absolute; left: 0; top: 44px; width: 196px; height: 432px;
    background: var(--panel-dark);
  }
  .brand {
    position: absolute; left: 18px; top: 18px; width: 160px; height: 160px;
    background: var(--logo-bg);
    display: flex; align-items: center; justify-content: center;
    color: var(--text-main); font-weight: 700; font-size: 19px; letter-spacing: 2px;
  }
  .nav { position: absolute; left: 18px; top: 186px; width: 160px; list-style: none; }
  .nav li { height: 45px; padding-top: 8px; border-bottom: 1px solid var(--divider); }
  .nav li.nav-home { height: 26px; padding-top: 0; }
  .nav li:last-child { border-bottom: none; }
  .nav-title { display: block; color: var(--text-main); font-size: 13px; line-height: 15px; letter-spacing: 0.2px; }
  .nav-sub { display: block; color: var(--text-sub); font-size: 9.5px; line-height: 12px; }
  .footer {
    position: absolute; left: 0; top: 373px; width: 196px; height: 59px;
    border-top: 1px dashed #4a4a4a;
  }
  .social { position: absolute; left: 15px; top: 19px; display: flex; gap: 3px; }
  .social svg { width: 22px; height: 22px; display: block; }
  .footer-rule { position: absolute; left: 102px; top: 17px; width: 1px; height: 24px; background: var(--divider); }
  .copyright {
    position: absolute; left: 108px; top: 20px; width: 68px;
    text-align: center; color: var(--copy-text); font-size: 8px; line-height: 10px;
  }
</style>
</head>
<body>
<div class="site">
  <div class="hero" role="img" aria-label="Concert stage with bright orange spotlights above a cheering crowd"></div>
  <aside class="sidebar">
    <div class="sidebar-body">
      <div class="brand">Plumtree</div>
      <ul class="nav">
        <li class="nav-home"><span class="nav-title">HOME</span></li>
        <li><span class="nav-title">ABOUT US</span><span class="nav-sub">We put our hearts</span></li>
        <li><span class="nav-title">ORDER TICKETS</span><span class="nav-sub">Get Tickets Online</span></li>
        <li><span class="nav-title">CONTACT</span><span class="nav-sub">Get in Touch</span></li>
      </ul>
      <div class="footer">
        <div class="social">
          <svg viewBox="0 0 22 22" aria-label="News feed"><circle cx="11" cy="11" r="11" fill="#333"/><circle cx="7.5" cy="14.5" r="1.6" fill="#121212"/><path d="M6 10.5a5.5 5.5 0 0 1 5.5 5.5M6 7a9 9 0 0 1 9 9" stroke="#121212" stroke-width="1.8" fill="none"/></svg>
          <svg viewBox="0 0 22 22" aria-label="Message us"><circle cx="11" cy="11" r="11" fill="#333"/><path d="M6 7h10v6.5h-5.5l-3 2.5v-2.5H6z" fill="#121212"/></svg>
          <svg viewBox="0 0 22 22" aria-label="Share"><circle cx="11" cy="11" r="11" fill="#333"/><circle cx="7" cy="11" r="1.8" fill="#121212"/><circle cx="14.5" cy="7" r="1.8" fill="#121212"/><circle cx="14.5" cy="15" r="1.8" fill="#121212"/><path d="M7 11l7.5-4M7 11l7.5 4" stroke="#121212" stroke-width="1.3"/></svg>
        </div>
        <div class="footer-rule"></div>
        <div class="copyright">© Copyright<br>2014</div>
      </div>
    </div>
  </aside>
</div>
</body>
</html>
```